business card design

Hey I would like a business design, please incorporate my business logo and services on it. Please check my website for ideas www.fernvalearborists.com.au
Thanks

Industry/Entity Type

Business

Contact Information for Business Card

company logo

Requirements
Must have
• website url
• email address which is fernvalearborists@mailbox-example.com
Should not have
• company logo

```html
<!DOCTYPE html>
<html lang="en">
<head>
<meta charset="utf-8">
<title>Fernvale Arborists – Business Card</title>
<link href="https://fonts.googleapis.com/css2?family=Roboto+Condensed:wght@400;700&display=swap" rel="stylesheet">
<style>
  :root {
    --backdrop: #ecebe7;
    --card-white: #ffffff;
    --navy: #1f2a44;
    --leaf-green: #169c4c;
    --name-green: #1a9a4c;
    --deep-green: #118a41;
    --text-white: #ffffff;
    --ink: #1d1d1d;
  }
  * { margin: 0; padding: 0; box-sizing: border-box; }
  html, body { width: 1200px; height: 1000px; overflow: hidden; }
  body {
    background: var(--backdrop);
    font-family: "Roboto Condensed", Arial, sans-serif;
    position: relative;
  }
  .card {
    position: absolute;
    left: 340px;
    width: 520px;
    height: 296px;
    box-shadow: 0 4px 14px rgba(0,0,0,0.18);
  }
  .card-front { top: 170px; background: var(--card-white); }
  .card-back { top: 520px; background: var(--leaf-green); overflow: hidden; }

  .brand {
    position: absolute;
    left: 36px;
    top: 112px;
    width: 190px;
    display: flex;
    align-items: center;
    gap: 10px;
  }
  .brand-dot {
    flex: none;
    width: 22px; height: 22px; border-radius: 50%;
    background: var(--leaf-green);
  }
  .brand-name {
    font-weight: 700;
    font-size: 30px;
    line-height: 1.05;
    color: var(--navy);
    text-transform: uppercase;
    letter-spacing: 0.5px;
  }

  .person { position: absolute; left: 248px; top: 80px; white-space: nowrap; }
  .person-name {
    font-weight: 700; font-size: 29px; color: var(--navy); line-height: 1;
  }
  .person-name .surname { color: var(--name-green); }
  .person-role { font-size: 16px; color: var(--ink); margin-top: 8px; line-height: 1.2; }
  .contact { list-style: none; margin-top: 22px; font-size: 14.5px; color: var(--ink); line-height: 1.25; }

  .watermark {
    position: absolute;
    right: 14px;
    bottom: 12px;
    font-weight: 700;
    line-height: 1;
    color: var(--deep-green);
    text-transform: uppercase;
    text-align: right;
  }
  .watermark-main { display: block; font-size: 44px; }
  .watermark-sub { display: block; font-size: 26px; letter-spacing: 1px; }
  .services {
    position: absolute;
    left: 37px;
    top: 80px;
    display: grid;
    grid-template-columns: 193px auto;
    row-gap: 29px;
    list-style: none;
    color: var(--text-white);
    font-size: 17.5px;
    line-height: 21px;
  }
</style>
</head>
<body>
  <section class="card card-front">
    <div class="brand">
      <span class="brand-dot"></span>
      <span class="brand-name">Fernvale<br>Arborists</span>
    </div>
    <div class="person">
      <p class="person-name">SAM <span class="surname">WARD</span></p>
      <p class="person-role">Principal</p>
      <ul class="contact">
        <li>123 456 7890</li>
        <li>fernvalearborists@mailbox-example.com</li>
        <li>www.fernvalearborists.com.au</li>
      </ul>
    </div>
  </section>

  <section class="card card-back">
    <div class="watermark">
      <span class="watermark-main">Fernvale</span>
      <span class="watermark-sub">Arborists</span>
    </div>
    <ul class="services">
      <li>Tree Removal</li>
      <li>Tree Shaping and Hedge Trimming</li>
      <li>Stump Grinding</li>
      <li>Palm Cleaning and Removals</li>
      <li>Block Clearing</li>
      <li>Emergency Damage Repairs</li>
    </ul>
  </section>
</body>
</html>
```